New "above the fold" design for our website

We would like to see some new creative designs for our above the fold section on our homepage. We are an online marketplace for fresh produce and meat.

You must design the desktop and mobile layouts.

Target Market(s)

Women 30-45 years old who buy groceries, with 2 children under 10 years old.

Industry/Entity Type

Grocery Store

Number of Pages Required

1 page

Font styles to use
Sans Serif

Requirements
Must have
• Give customers the sense of organic and farm fresh as we are battling the big supermarket chains.
Nice to have
• Pictures of produce. Pictures of farmers.

```html
<!DOCTYPE html>
<html lang="en">
<head>
<meta charset="utf-8">
<title>Fieldhand – Best Quality Farm Grown Produce</title>
<link href="https://fonts.googleapis.com/css2?family=Montserrat:wght@400;500;600;700&family=Arimo:wght@400;700&display=swap" rel="stylesheet">
<style>
  :root {
    --red: #e8141c;
    --search-grey: #c9cbce;
    --nav-bg: #f3f3f3;
    --nav-text: #3a3a3a;
    --brand-green: #4b6b27;
    --orange: #f68b33;
    --teal: #46b98b;
    --mustard: #e7ab2d;
    --leaf: #7dc63c;
    --strip-grey: #c8c8c8;
    --stats-bg: rgba(240, 240, 236, 0.93);
    --stats-text: #4a4a4a;
    --accent-yellow: #fbe36a;
    --button-yellow: #f6c844;
    --white: #ffffff;
  }
  * { box-sizing: border-box; margin: 0; padding: 0; }
  html, body { width: 1200px; height: 567px; overflow: hidden; background: var(--white); }
  body { position: relative; font-family: "Montserrat", sans-serif; }

  .hero-photo {
    position: absolute; left: 0; top: 0; width: 1200px; height: 510px;
    background:
      radial-gradient(ellipse 220px 340px at 1050px 330px, rgba(70,110,60,0.55), transparent 70%),
      linear-gradient(180deg, #9fb6c6 0%, #c9c6ae 22%, #a89a72 34%, #7e8c4c 46%, #6f9a3a 62%, #5f8d2e 80%, #4f7a28 100%);
  }

  .login-btn {
    position: absolute; left: 792px; top: 15px; width: 124px; height: 27px;
    background: var(--red); color: var(--white); border-radius: 3px;
    font: 600 11px/27px "Montserrat", sans-serif; text-align: center; letter-spacing: 0.3px;
  }
  .search-btn {
    position: absolute; left: 923px; top: 14px; width: 30px; height: 30px;
    border-radius: 50%; background: var(--search-grey);
  }
  .search-btn svg { position: absolute; left: 9px; top: 9px; }

  .main-nav {
    position: absolute; left: 249px; top: 54px; width: 705px; height: 51px;
    background: var(--nav-bg);
  }
  .nav-link {
    position: absolute; top: 0; height: 51px; line-height: 47px;
    font-weight: 500; font-size: 10.5px; color: var(--nav-text); text-align: center;
    border-bottom: 4px solid; white-space: nowrap;
  }
  .nav-how { left: 0; width: 133px; border-color: var(--orange); }
  .nav-about { left: 133px; width: 109px; border-color: var(--teal); }
  .nav-gap-left { left: 242px; width: 19px; border-color: var(--strip-grey); }
  .nav-gap-right { left: 444px; width: 19px; border-color: var(--strip-grey); }
  .nav-products { left: 463px; width: 120px; border-color: var(--mustard); }
  .nav-contact { left: 583px; width: 122px; border-color: var(--leaf); }

  .brand {
    position: absolute; left: 510px; top: 30px; width: 183px; height: 96px;
    background: var(--white); text-align: center; color: var(--brand-green);
  }
  .brand-name { margin-top: 30px; font: 600 20px/1 "Montserrat", sans-serif; letter-spacing: 1.5px; }
  .brand-tagline { margin-top: 8px; font: 600 7.5px/1 "Montserrat", sans-serif; letter-spacing: 0.8px; white-space: nowrap; }

  .headline {
    position: absolute; left: 0; top: 168px; width: 1200px; text-align: center;
    font-weight: 500; font-size: 34px; line-height: 1; color: var(--white);
    text-shadow: 0 1px 4px rgba(0,0,0,0.25);
  }

  .slide-arrow { position: absolute; top: 224px; }
  .slide-prev { left: 32px; }
  .slide-next { left: 1132px; }

  .stats-bar {
    position: absolute; left: 248px; top: 350px; width: 703px; height: 28px;
    background: var(--stats-bg);
    font-weight: 500; font-size: 12px; color: var(--stats-text);
  }
  .stat { position: absolute; top: 0; height: 28px; display: flex; align-items: center; gap: 12px; white-space: nowrap; }
  .stat-orders { left: 29px; }
  .stat-customers { left: 198px; }
  .stat-likes { left: 385px; }
  .stat-followers { left: 532px; }

  .feature-cards { position: absolute; left: 248px; top: 378px; width: 703px; height: 187px; display: flex; }
  .card { position: relative; width: 176px; height: 187px; color: var(--white); }
  .card-price { background: var(--orange); }
  .card-delivery { background: var(--teal); width: 175px; }
  .card-fresh { background: var(--mustard); width: 175px; }
  .card-organic { background: var(--leaf); }
  .card > * { position: absolute; left: 19px; }
  .card-organic > * { left: 17px; }
  .card-title { top: 14px; font-weight: 700; font-size: 23.5px; line-height: 1; white-space: nowrap; }
  .card-subtitle { top: 40px; font-weight: 500; font-size: 20px; line-height: 1; color: var(--accent-yellow); white-space: nowrap; }
  .card-body {
    top: 80px; width: 148px; padding-left: 3px;
    font: 400 11px/15px "Arimo", sans-serif;
  }
  .read-more {
    top: 165px; padding-left: 5px;
    font: 700 11.5px/1 "Arimo", sans-serif; white-space: nowrap;
  }
  .card-delivery .lead { top: 79px; font: 400 12px/1 "Arimo", sans-serif; white-space: nowrap; }
  .card-delivery .lead-caps { top: 98px; font: 400 10.5px/1 "Arimo", sans-serif; letter-spacing: 0.2px; white-space: nowrap; }
  .postcode {
    top: 124px; width: 147px; height: 21px; border: 1px solid var(--white);
    color: var(--white); padding-left: 7px;
    font: 400 11px/19px "Arimo", sans-serif;
  }
  .shop-now {
    top: 152px; width: 77px; height: 21px; background: var(--button-yellow);
    color: var(--white); font: 400 11px/21px "Arimo", sans-serif; text-align: center; letter-spacing: 0.4px;
  }
</style>
</head>
<body>
  <div class="hero-photo" role="img" aria-label="Photo of green farm rows and hills under a hazy sky, with a farmer in a straw hat and apron holding a crate of fresh vegetables on the right"></div>

  <div class="login-btn">LOGIN/REGISTER</div>
  <div class="search-btn">
    <svg width="12" height="12" viewBox="0 0 12 12"><circle cx="5" cy="5" r="3.6" fill="none" stroke="#333" stroke-width="1.8"/><line x1="7.7" y1="7.7" x2="11" y2="11" stroke="#333" stroke-width="2" stroke-linecap="round"/></svg>
  </div>

  <nav class="main-nav">
    <div class="nav-link nav-how">HOW IT WORKS</div>
    <div class="nav-link nav-about">ABOUT US</div>
    <div class="nav-link nav-gap-left"></div>
    <div class="nav-link nav-gap-right"></div>
    <div class="nav-link nav-products">PRODUCTS</div>
    <div class="nav-link nav-contact">CONTACT</div>
  </nav>

  <div class="brand">
    <div class="brand-name">FIELDHAND</div>
    <div class="brand-tagline">THE NEIGHBOURHOOD GROCER</div>
  </div>

  <h1 class="headline">Best Quality Farm Grown Produce</h1>

  <svg class="slide-arrow slide-prev" width="28" height="60" viewBox="0 0 28 60"><polyline points="25,2 3,30 25,58" fill="none" stroke="#fff" stroke-width="2"/></svg>
  <svg class="slide-arrow slide-next" width="28" height="60" viewBox="0 0 28 60"><polyline points="3,2 25,30 3,58" fill="none" stroke="#fff" stroke-width="2"/></svg>

  <div class="stats-bar">
    <div class="stat stat-orders">
      <svg width="18" height="18" viewBox="0 0 18 18"><rect x="4" y="6" width="10" height="11" fill="#f68b33"/><rect x="0" y="6" width="18" height="3" fill="#f68b33"/><rect x="8" y="0" width="2" height="6" fill="#f68b33"/></svg>
      <span>34500 ORDERS</span>
    </div>
    <div class="stat stat-customers">
      <svg width="18" height="18" viewBox="0 0 18 18"><path d="M1 9 H17 L14 17 H4 Z" fill="#46b98b"/><circle cx="14" cy="4" r="3.5" fill="none" stroke="#46b98b" stroke-width="1.6"/></svg>
      <span>10093 CUSTOMERS</span>
    </div>
    <div class="stat stat-likes">
      <svg width="16" height="16" viewBox="0 0 16 16"><rect x="0" y="7" width="3.5" height="9" fill="#e7ab2d"/><path d="M5 7 L9 1 Q11 1 10.5 4 L10 6 H15 Q16 7 15 9 L13 15 H5 Z" fill="#e7ab2d"/></svg>
      <span>10277 LIKES</span>
    </div>
    <div class="stat stat-followers">
      <svg width="15" height="15" viewBox="0 0 15 15"><rect width="15" height="15" fill="#7dc63c"/></svg>
      <span>4430 FOLLOWERS</span>
    </div>
  </div>

  <section class="feature-cards">
    <article class="card card-price">
      <h2 class="card-title">Best Price</h2>
      <p class="card-subtitle">Always</p>
      <p class="card-body">Corporis suscipit laboriosam, nisi ut aliquid ex ea commodi cons equat ur, Quis autemvel illum qui dolorem</p>
      <span class="read-more">Read More &nbsp;›</span>
    </article>
    <article class="card card-delivery">
      <h2 class="card-title">Delivery</h2>
      <p class="card-subtitle">Quick</p>
      <p class="lead">Quality Meat &amp; Produce</p>
      <p class="lead-caps">DELIVERED TO YOUR DOOR</p>
      <div class="postcode">Enter postcode</div>
      <div class="shop-now">SHOP NOW</div>
    </article>
    <article class="card card-fresh">
      <h2 class="card-title">Farm Fresh</h2>
      <p class="card-subtitle">Quality</p>
      <p class="card-body">Nam libero tempore, cum soluta nobis est eligendi optio cumque nihil impedit quo minus id quod maxime</p>
      <span class="read-more">Read More &nbsp;›</span>
    </article>
    <article class="card card-organic">
      <h2 class="card-title">Organic</h2>
      <p class="card-subtitle">100% Healthy</p>
      <p class="card-body">Accusamus et iusto odio dignissimos ducimus qui blanditiis praesentium voluptatum deleniti</p>
      <span class="read-more">Read More &nbsp;›</span>
    </article>
  </section>
</body>
</html>
```